TrueGrindz Complete Stationery - Logo already designed

I already have the logo designed see attached. I need have a full set of stationary and business card designed for printing. I have attached an example of what I mean.

Please feel free to be creative. Also you can use the X in the logo by its self if you think it will work.

My details:

Name: Corwin Lestak
Social media handles: @corwinlestak
W: corwinlestak.com
E: info@corwinlestak.com
​P: 08 7493 5286
PO Box 7382, Scarborough 6019
ABN 83 402 719 265

Target Market(s)

Anyone looking to be inspired.

Industry/Entity Type

Business

Font styles to use
Sans Serif

Colors
fbee3e
000000

Requirements
Must have
• My details:
• Name: Corwin Lestak
• Social media handles: @corwinlestak
• W: corwinlestak.com
• E: info@corwinlestak.com
• ​P: 08 7493 5286
• PO Box 7382, Scarborough 6019
• ABN 83 402 719 265
Nice to have
• Something a little different
Should not have
• must not look tacky.

```html
<!DOCTYPE html>
<html lang="en">
<head>
<meta charset="utf-8">
<title>TrueGrindz Stationery</title>
<link rel="stylesheet" href="https://fonts.googleapis.com/css2?family=Oswald:wght@600&family=Open+Sans:wght@400;600;700&display=swap">
<style>
  :root {
    --bg: #5e6165;
    --paper: #ffffff;
    --ink: #000000;
    --ink-soft: #3a3a3a;
    --muted: #7a7a7a;
    --yellow: #fbee3e;
    --gold: #f2b705;
    --charcoal: #232323;
    --band: #0c0c0c;
    --disc-hub: #6b6d70;
  }
  * { margin: 0; padding: 0; box-sizing: border-box; }
  html, body { width: 1200px; height: 900px; overflow: hidden; }
  body {
    background: var(--bg);
    font-family: "Open Sans", Arial, sans-serif;
    color: var(--ink);
    position: relative;
  }
  .piece { position: absolute; box-shadow: 0 4px 14px rgba(0,0,0,.35); }
  .wordmark {
    font-family: "Oswald", "Arial Narrow", sans-serif;
    font-weight: 600;
    text-transform: uppercase;
    letter-spacing: .02em;
    line-height: 1;
  }
  .wordmark--dark { color: var(--ink); }
  .wordmark--light { color: var(--paper); }

  /* Letterhead */
  .letterhead {
    left: 40px; top: 40px; width: 360px; height: 509px;
    background: var(--paper);
    padding: 30px 32px;
    font-size: 6.6px; line-height: 1.6;
    color: var(--ink-soft);
  }
  .letterhead__top { display: flex; justify-content: space-between; align-items: flex-start; }
  .letterhead__sender { font-size: 6px; line-height: 1.55; color: var(--muted); }
  .letterhead__sender strong { color: var(--ink); font-weight: 700; display: block; }
  .letterhead .wordmark { font-size: 20px; }
  .letterhead__body { margin-top: 62px; }
  .letterhead__body p { margin-bottom: 10px; }
  .signature { display: block; margin-top: 40px; width: 90px; height: 26px; }

  /* Presentation folder */
  .folder {
    left: 430px; top: 40px; width: 360px; height: 509px;
    background: var(--charcoal);
    overflow: hidden;
  }
  .folder svg { position: absolute; inset: 0; }
  .folder .wordmark { position: absolute; left: 34px; bottom: 42px; font-size: 30px; }

  /* Business cards */
  .card { left: 820px; width: 340px; height: 195px; }
  .card--front { top: 40px; background: var(--paper); padding: 22px 24px; }
  .card--front .wordmark { font-size: 22px; }
  .card__person { position: absolute; right: 24px; top: 70px; text-align: right; }
  .card__name { font-weight: 700; font-size: 13px; color: var(--gold); }
  .card__role { font-size: 8px; color: var(--muted); margin-top: 2px; }
  .card__contact {
    position: absolute; right: 24px; bottom: 20px; text-align: right;
    font-size: 7.5px; line-height: 1.6; color: var(--ink-soft);
  }
  .card--back { top: 255px; background: var(--charcoal); overflow: hidden; }
  .card--back svg { position: absolute; inset: 0; }
  .card--back .wordmark {
    position: absolute; left: 0; right: 0; top: 50%; transform: translateY(-50%);
    text-align: center; font-size: 30px;
  }

  /* Envelope */
  .envelope {
    left: 40px; top: 590px; width: 580px; height: 280px;
    background: var(--paper);
    padding: 26px 30px;
    overflow: hidden;
  }
  .envelope .wordmark { font-size: 18px; }
  .envelope__return { margin-top: 14px; font-size: 6.5px; line-height: 1.6; color: var(--muted); }
  .envelope__return strong { color: var(--ink); font-weight: 700; display: block; }
  .envelope__flap {
    position: absolute; right: 0; top: 0; bottom: 0; width: 60px;
    background: var(--band);
    border-radius: 30px 0 0 30px;
  }

  /* Disc */
  .disc {
    left: 660px; top: 590px; width: 280px; height: 280px;
    border-radius: 50%;
    background: var(--paper);
  }
  .disc__hub {
    position: absolute; left: 50%; top: 50%; width: 84px; height: 84px;
    margin: -42px 0 0 -42px; border-radius: 50%; background: var(--disc-hub);
  }
  .disc__hole {
    position: absolute; left: 50%; top: 50%; width: 30px; height: 30px;
    margin: -15px 0 0 -15px; border-radius: 50%; background: var(--bg);
  }
</style>
</head>
<body>

<section class="piece letterhead">
  <div class="letterhead__top">
    <div class="letterhead__sender">
      <strong>Corwin Lestak</strong>
      PO Box 7382, Scarborough 6019<br>
      P: 08 7493 5286<br>
      E: info@corwinlestak.com<br>
      W: corwinlestak.com<br>
      ABN 83 402 719 265
    </div>
    <div class="wordmark wordmark--dark">TrueGrindz</div>
  </div>
  <div class="letterhead__body">
    <p>Thank you for choosing to train with us this season. Every session is built to push you a little further than the last, and we are proud to walk that road beside you.</p>
    <p>Our coaches will meet you each week to review your goals, track progress and adjust the plan where needed. Bring water, a towel and the right attitude.</p>
    <p>We look forward to seeing what you achieve. Start today and keep going.</p>
    <svg class="signature" role="img" aria-label="Handwritten signature of Corwin Lestak" viewBox="0 0 90 26">
      <rect width="90" height="26" fill="#e4e4e4"/>
    </svg>
  </div>
</section>

<section class="piece folder">
  <svg viewBox="0 0 360 509" preserveAspectRatio="none" aria-hidden="true">
    <polygon points="120,0 200,0 20,509 -60,509" fill="var(--band)"/>
    <polygon points="250,0 300,0 120,509 70,509" fill="var(--band)"/>
  </svg>
  <div class="wordmark wordmark--light">TrueGrindz</div>
</section>

<section class="piece card card--front">
  <div class="wordmark wordmark--dark">TrueGrindz</div>
  <div class="card__person">
    <div class="card__name">Corwin Lestak</div>
    <div class="card__role">Founder</div>
  </div>
  <div class="card__contact">
    PO Box 7382, Scarborough 6019<br>
    P: 08 7493 5286 &nbsp; E: info@corwinlestak.com<br>
    W: corwinlestak.com &nbsp; @corwinlestak<br>
    ABN 83 402 719 265
  </div>
</section>

<section class="piece card card--back">
  <svg viewBox="0 0 340 195" preserveAspectRatio="none" aria-hidden="true">
    <polygon points="60,0 120,0 50,195 -10,195" fill="var(--band)"/>
    <polygon points="160,0 195,0 125,195 90,195" fill="var(--band)"/>
  </svg>
  <div class="wordmark wordmark--light">TrueGrindz</div>
</section>

<section class="piece envelope">
  <div class="wordmark wordmark--dark">TrueGrindz</div>
  <div class="envelope__return">
    <strong>Corwin Lestak</strong>
    PO Box 7382, Scarborough 6019<br>
    P: 08 7493 5286<br>
    E: info@corwinlestak.com<br>
    W: corwinlestak.com
  </div>
  <div class="envelope__flap"></div>
</section>

<section class="piece disc">
  <div class="disc__hub"></div>
  <div class="disc__hole"></div>
</section>

</body>
</html>
```